Business Card design for new private practice opening

I need a business card design for my new private practice with my new logo uploaded as a file
On the front the logo
On the back: maybe a small logo somewhere?
Priv. Doz. DDr. Corinna Vestaluk
Fachärztin für Allgemein- & Viszeralchirurgie
Address: xxx
Tel: xxx
Mobil:xxx
Webseite:xxx
Email:xxx

Contact Information for Business Card

See project description above for details

Requirements
Nice to have
• I would like the colors of the logo incorporated into the business card

```html
<!DOCTYPE html>
<html lang="de">
<head>
<meta charset="utf-8">
<title>Vestaluk Chirurgie – Visitenkarte</title>
<link href="https://fonts.googleapis.com/css2?family=Montserrat:wght@400;500;600;700&display=swap" rel="stylesheet">
<style>
  :root {
    --teal: #47b8b6;
    --teal-dark: #36a3a1;
    --paper: #f4f4f4;
    --backdrop: #e6e6e6;
    --ink: #6a6a6a;
    --rule: #9a9a9a;
    --white: #ffffff;
  }
  * { margin: 0; padding: 0; box-sizing: border-box; }
  html, body {
    width: 1200px; height: 1000px; overflow: hidden;
    background: var(--backdrop);
    font-family: "Montserrat", sans-serif;
  }
  .canvas { position: relative; width: 1200px; height: 1000px; }

  .card {
    position: absolute;
    width: 600px; height: 364px;
    border-radius: 32px;
    overflow: hidden;
  }
  .card--front { left: 300px; top: 108px; background: var(--teal); }
  .card--back { left: 300px; top: 526px; background: var(--paper); }

  .brand { position: absolute; display: flex; align-items: center; gap: 10px; }
  .brand__dot { border-radius: 50%; flex: none; }
  .brand__name { font-weight: 600; line-height: 1.08; letter-spacing: 0.3px; }

  .card--front .brand { left: 363px; top: 276px; }
  .card--front .brand__dot { width: 54px; height: 54px; border: 2px solid var(--white); }
  .card--front .brand__name { color: var(--white); font-size: 21px; }

  .card--back .brand { left: 200px; top: 57px; }
  .card--back .brand__dot { width: 58px; height: 58px; background: var(--teal); border: 2px solid var(--ink); }
  .card--back .brand__name { color: var(--ink); font-size: 23px; font-weight: 500; }

  .identity {
    position: absolute; right: 319px; top: 171px;
    text-align: right; white-space: nowrap;
  }
  .identity__title { color: var(--teal); font-weight: 700; font-size: 18px; line-height: 26px; }
  .identity__name { color: var(--teal); font-weight: 700; font-size: 18px; line-height: 26px; text-transform: uppercase; }
  .identity__role { color: var(--ink); font-size: 13.5px; line-height: 18px; margin-top: 2px; }

  .divider {
    position: absolute; left: 300px; top: 162px;
    width: 1.5px; height: 102px; background: var(--teal);
  }

  .contacts { position: absolute; left: 324px; top: 170px; list-style: none; }
  .contacts li {
    display: flex; align-items: center; gap: 10px;
    height: 21.5px; color: var(--ink); font-size: 13.5px;
  }
  .contacts svg { width: 14px; height: 14px; fill: var(--teal); flex: none; }

  .footer-rule {
    position: absolute; left: 33px; right: 33px; top: 307px;
    height: 1px; background: var(--rule);
  }
  .location {
    position: absolute; left: 0; right: 0; top: 330px;
    display: flex; justify-content: center; align-items: center; gap: 6px;
    color: var(--ink); font-size: 14px;
  }
  .location svg { width: 12px; height: 16px; fill: var(--teal); }
</style>
</head>
<body>
<div class="canvas">

  <section class="card card--front">
    <div class="brand">
      <span class="brand__dot"></span>
      <span class="brand__name">VESTALUK<br>CHIRURGIE</span>
    </div>
  </section>

  <section class="card card--back">
    <div class="brand">
      <span class="brand__dot"></span>
      <span class="brand__name">VESTALUK<br>CHIRURGIE</span>
    </div>

    <div class="identity">
      <p class="identity__title">Priv. Doz. DDr.</p>
      <p class="identity__name">Corinna Vestaluk</p>
      <p class="identity__role">Fachärztin für Allgemein-<br>&amp; Viszeralchirurgie</p>
    </div>

    <div class="divider"></div>

    <ul class="contacts">
      <li>
        <svg viewBox="0 0 24 24"><path d="M6.6 10.8a15 15 0 0 0 6.6 6.6l2.2-2.2a1 1 0 0 1 1-.25 11.4 11.4 0 0 0 3.6.57 1 1 0 0 1 1 1V20a1 1 0 0 1-1 1A17 17 0 0 1 3 4a1 1 0 0 1 1-1h3.5a1 1 0 0 1 1 1c0 1.25.2 2.45.57 3.57a1 1 0 0 1-.25 1z"/></svg>
        Tel: xxx
      </li>
      <li>
        <svg viewBox="0 0 24 24"><rect x="6" y="1" width="12" height="22" rx="2"/><circle cx="12" cy="19" r="1.2" fill="#f4f4f4"/></svg>
        Mobil:xxx
      </li>
      <li>
        <svg viewBox="0 0 24 24"><path d="M12 2a10 10 0 1 0 0 20 10 10 0 0 0 0-20zm6.9 6h-2.9a15.6 15.6 0 0 0-1.4-3.6A8 8 0 0 1 18.9 8zM12 4c.8 1.2 1.5 2.5 1.9 4h-3.8c.4-1.4 1.1-2.8 1.9-4zM4.3 14a8 8 0 0 1 0-4h3.4a16 16 0 0 0 0 4zm.8 2h3a15.6 15.6 0 0 0 1.3 3.6A8 8 0 0 1 5.1 16zM8 8H5.1a8 8 0 0 1 4.3-3.6A15.6 15.6 0 0 0 8 8zm4 12c-.8-1.2-1.5-2.5-1.9-4h3.8c-.4 1.4-1.1 2.8-1.9 4zm2.3-6H9.7a14.7 14.7 0 0 1 0-4h4.6a14.7 14.7 0 0 1 0 4zm.3 5.6A15.6 15.6 0 0 0 16 16h2.9a8 8 0 0 1-4.3 3.6zM16.3 14a16 16 0 0 0 0-4h3.4a8 8 0 0 1 0 4z"/></svg>
        Webseite:xxx
      </li>
      <li>
        <svg viewBox="0 0 24 24"><path d="M2 5h20v14H2zm2 2v.5l8 5.5 8-5.5V7l-8 5.5z"/></svg>
        Email:xxx
      </li>
    </ul>

    <div class="footer-rule"></div>

    <p class="location">
      <svg viewBox="0 0 12 16"><path d="M6 0a6 6 0 0 0-6 6c0 4.5 6 10 6 10s6-5.5 6-10a6 6 0 0 0-6-6zm0 8.3A2.3 2.3 0 1 1 6 3.7a2.3 2.3 0 0 1 0 4.6z"/></svg>
      Austria
    </p>
  </section>

</div>
</body>
</html>
```